Flyer for American Indian Elders on Dementia Warning Signs

We need a flyer designed for older adults who are American Indian or Alaska Native (in the U.S.).

Ideally, the flyer should complement the colors of our logos. The project logo and our organization logo are attached to the brief.

When people see the flyer we want them to feel that it represents their culture, is warm, and professional but relatable to older adults and people who have limited incomes.

I have attached an earlier draft of the document we designed ourselves BUT we want different and better.

It is for older adults who have trouble reading so:
1. you must use a font that is 11.5 points or larger
2. Do not put text over complex pictures or use shading with words
3. You can use a serif font for the heading, but should use san serif for the body text
4. There should be good contrast between the font color and background

Please do not use any images that include a head dress or pictures of American Indian people or things that are very traditional or "token" imagery.

We need to save a small space under the call out box/ somewhere on the flyer for other people to add their logo once they download.

Let us know if you have questions or need additional information.

Target Market(s)

Older American Indian people

Font styles to use
Serif
Sans Serif

Requirements
Must have
• Easy to read for older adults
Should not have
• indian headdress

```html
<!DOCTYPE html>
<html lang="en">
<head>
<meta charset="utf-8">
<title>10 Signs of Thinking or Memory Changes that Might be Dementia</title>
<link rel="stylesheet" href="https://fonts.googleapis.com/css2?family=Roboto+Condensed:wght@300;400;700&family=Montserrat:wght@400;500;600&display=swap">
<style>
  :root {
    --teal-deep: #0e6368;
    --teal-light: #4ba8af;
    --red: #c8574b;
    --red-dark: #a8463c;
    --list-grey: #ececec;
    --photo-dark: #5f5f5f;
    --photo-light: #8d8d8d;
    --ink: #1d1d1d;
    --white: #ffffff;
    --accent-dot: #4fc3c8;
  }
  * { box-sizing: border-box; margin: 0; padding: 0; }
  html, body { width: 900px; height: 1200px; overflow: hidden; background: var(--white); }
  .flyer {
    position: relative; width: 900px; height: 1200px; overflow: hidden;
    font-family: "Roboto Condensed", "Arial Narrow", sans-serif; color: var(--ink);
  }
  .top-band { position: absolute; left: 0; top: 0; width: 900px; height: 97px; background: var(--teal-deep); }
  .brand {
    position: absolute; left: 0; top: 0; width: 307px; height: 97px; background: var(--white);
    display: flex; align-items: center; gap: 12px; padding-left: 40px;
  }
  .brand-mark { width: 36px; height: 36px; border-radius: 50%; background: var(--teal-deep); flex: none; }
  .brand-name {
    font-family: "Roboto Condensed", sans-serif; font-weight: 700; font-size: 16px;
    line-height: 1.15; color: var(--teal-deep); text-transform: uppercase;
  }
  .hero-photo {
    position: absolute; left: 0; top: 97px; width: 900px; height: 502px;
    background: linear-gradient(100deg, var(--photo-light) 0%, #a9a9a9 40%, var(--photo-dark) 70%, #3a3a3a 100%);
  }
  .lower-teal { position: absolute; left: 307px; top: 599px; width: 593px; height: 601px; background: var(--teal-deep); }
  .intro {
    position: absolute; left: 39px; top: 127px; width: 501px; height: 276px;
    background: var(--teal-light); color: var(--white); padding: 18px 26px;
  }
  .intro-title { font-weight: 300; font-size: 22px; line-height: 1.2; }
  .intro-title strong { display: block; font-weight: 700; font-size: 26px; }
  .intro p { font-weight: 300; font-size: 16px; line-height: 1.3; margin-top: 14px; }
  .intro p + p { margin-top: 10px; }
  .signs {
    position: absolute; left: 39px; top: 422px; width: 497px; height: 760px;
    background: var(--list-grey); padding: 22px 24px 0 34px;
    list-style: none; counter-reset: sign;
  }
  .signs li {
    position: relative; counter-increment: sign; font-size: 15.5px; line-height: 1.32;
    padding-left: 22px; margin-bottom: 18px;
  }
  .signs li::before {
    content: counter(sign) "."; position: absolute; left: -10px; width: 28px; text-align: right; font-weight: 700;
  }
  .signs li:nth-child(10)::before { left: -16px; }
  .signs strong { font-weight: 700; }
  .main-points {
    position: absolute; left: 567px; top: 526px; width: 295px; height: 654px;
    background: var(--red); color: var(--white); padding: 26px 22px 0 22px;
  }
  .main-points h2 { font-weight: 700; font-size: 27px; margin-bottom: 20px; }
  .main-points ul { list-style: none; }
  .main-points li {
    position: relative; padding-left: 16px; font-size: 15.5px; line-height: 1.32; margin-bottom: 20px;
  }
  .main-points li::before {
    content: ""; position: absolute; left: 0; top: 6px; width: 5px; height: 5px; border-radius: 50%;
    background: var(--accent-dot);
  }
  .learn-more {
    position: absolute; left: 551px; top: 983px; width: 325px; height: 124px;
    background: var(--white); text-align: center; padding-top: 15px;
    font-family: "Montserrat", sans-serif; font-size: 13px; line-height: 1.4; color: var(--ink);
  }
  .learn-more .links { margin-top: 14px; font-style: italic; }
  .partner {
    position: absolute; left: 631px; top: 1117px; width: 173px; height: 43px; background: var(--white);
    display: flex; align-items: center; gap: 8px; padding-left: 8px;
  }
  .partner-mark { width: 26px; height: 26px; background: var(--teal-light); flex: none; }
  .partner-name { font-family: "Roboto Condensed", sans-serif; font-weight: 700; font-size: 12px; line-height: 1.1; color: var(--teal-deep); text-transform: uppercase; }
</style>
</head>
<body>
<main class="flyer">
  <div class="top-band"></div>
  <header class="brand">
    <span class="brand-mark"></span>
    <span class="brand-name">Northern Circle<br>Center for Brain Health</span>
  </header>

  <div class="hero-photo" role="img" aria-label="Black and white photograph of two elderly hands reaching toward each other"></div>
  <div class="lower-teal"></div>

  <section class="intro">
    <h1 class="intro-title">10 Signs of Thinking or Memory Changes <strong>that Might be Dementia</strong></h1>
    <p>As we get older, we may slow down a bit. This is a normal part of aging. Changes in memory or thinking that make it harder to get through the day, are not a normal part of aging. These may be early signs of dementia.</p>
    <p>Because American Indian and Alaska Native people have a high risk of dementia, it is important to know the warning signs. Do you have any of these 10 signs? If so, talk to your doctor.</p>
  </section>

  <ol class="signs">
    <li><strong>Memory loss that affects your daily life.</strong> You may forget events or important dates; repeat yourself; rely more often on lists or sticky notes to remember things more often</li>
    <li><strong>Trouble planning or solving problems.</strong> You may have a harder time paying bills; cooking recipes you have used for years</li>
    <li><strong>Get confused about the time, date, or where you are.</strong></li>
    <li><strong>Daily tasks are getting harder</strong>, including driving; making a grocery list or going shopping</li>
    <li><strong>Trouble with how your eyesight and thinking work together that gets worse.</strong> This includes tripping, falls, or problems with your balance; spilling or dropping things more</li>
    <li><strong>New trouble talking or writing.</strong> You have a hard time finding the words you want to say. For example, you may say “that thing on your wrist that tells time” instead of “watch.”</li>
    <li><strong>Lose and cannot find things.</strong> For example, you can’t find the coffee pot that you use every day; might put your car keys in the freezer</li>
    <li><strong>Notice changes in your mood or personality,</strong> such as being easily mad or sad in everyday situations; more fearful (scared) or suspicious (not trusting)</li>
    <li><strong>Act different and make poor choices.</strong> This may make you more likely to spend money you do not have or be a scam victim; stop washing up regularly or pay less attention to how you look; forget to take care of your pet</li>
    <li><strong>Pull away from friends and family because it is harder to keep up.</strong> You may not want to do things you used to enjoy, like sporting events, church, music, or sex.</li>
  </ol>

  <aside class="main-points">
    <h2>Main Points</h2>
    <ul>
      <li>American Indian and Alaska Native people have a higher risk of dementia.</li>
      <li>Big changes in memory or thinking that make it hard to get through the day are not a normal part of aging.</li>
      <li>People with one or more of these 10 signs should talk to their doctor to find the cause. It is not always dementia.</li>
      <li>Early dementia diagnosis gives you a chance to get care and plan your future.</li>
    </ul>
  </aside>

  <div class="learn-more">
    <p>To learn more about the warning signs<br>of dementia in American Indian and<br>Alaska Native people, visit:</p>
    <p class="links">www.northerncirclebrain.org<br>www.elderwellnessnet.org/aging</p>
  </div>

  <div class="partner">
    <span class="partner-mark"></span>
    <span class="partner-name">Council for<br>Elder Wellness</span>
  </div>
</main>
</body>
</html>
```